Graphics Design of Physics Book

Hi
Size : 8" x 11.25"
We are education book Publication Company and would like to have book cover for "Physics" it has 4 volumes. All 4 having the same color scheme and design except the volume no.
Blue is my personal favorite but u can use any color. Want to have a band at the bottom of the cover to place our Logo “VORLIN Education” a PDF of the same is attached, or you can place logo anywhere according to ur design.
I need “Physics” as title of the book to be visible prominently.
And volume and volume no. should also be Visible and eye catching I prefer a Graphic to enhance the Volume No.
A background pattern can also be a option (it should be vector form so that color can be change later)
Please do not offer any cut and paste design I need very professional presentation.
Volume and Number can be in metallic 3D (CMYK) effect.
only Professional presentation will get feedback.
I have provided a sample artwork for reference do not follow it but can be a reference what I needed !

Target Market(s)

Students Class 9th to 12th

Industry/Entity Type

Education

Font styles to use
Serif

Colors
3176b5
0555a3
85abd2
cadf82
abd036
9bcb3c

Requirements
Must have
• Eye catching.
• “Physics” as title of the book to be visible prominently.
• volume and volume no. should also be Visible and eye catching
• I prefer a Graphic to enhance the Volume No.
• Icons for
• 1. Questions and answers
• 2. Theory Notes
• 3. Tips & Tricks
• 4. Previous Year's Reference Questions
• 5. Covers Complete Syllabus
Nice to have
• decent seamless background or metallic 3d effect (not to be print in special Ink) design should only be in CMYK.
Should not have
• Physics related Pictures or Icons (Specially E=mc2) or any scientist photograph or I Need pure graphic design

```html
<!DOCTYPE html>
<html lang="en">
<head>
<meta charset="utf-8">
<title>Physics Volume 1 – Book Cover</title>
<link href="https://fonts.googleapis.com/css2?family=Anton&family=Cinzel:wght@600&family=Merriweather:wght@700&display=swap" rel="stylesheet">
<style>
  :root {
    --navy-deep: #23264f;
    --navy: #2c3166;
    --navy-glow: #3a3f8c;
    --stripe-light: #4f78bd;
    --stripe-mid: #3152a0;
    --stripe-dark: #24305e;
    --silver-light: #f4f4f4;
    --silver-dark: #5c5c60;
    --white: #ffffff;
    --ink: #111111;
  }
  * { margin: 0; padding: 0; box-sizing: border-box; }
  html, body { width: 861px; height: 1200px; overflow: hidden; background: var(--navy-deep); }
  .cover {
    position: relative; width: 861px; height: 1200px; overflow: hidden;
    background: radial-gradient(ellipse 520px 460px at 40% 52%, var(--navy-glow), var(--navy) 55%, var(--navy-deep) 100%);
  }
  .stripe-band {
    position: absolute; left: 0; width: 861px;
    background:
      linear-gradient(180deg, rgba(20,22,45,.55) 0%, rgba(20,22,45,0) 55%, rgba(20,22,45,.25) 100%),
      repeating-linear-gradient(90deg,
        var(--stripe-dark) 0 80px,
        var(--stripe-mid) 80px 100px,
        var(--stripe-light) 100px 150px,
        var(--stripe-mid) 150px 161px);
  }
  .stripe-band--top { top: 0; height: 120px; }
  .stripe-band--bottom { top: 990px; height: 210px;
    background:
      linear-gradient(0deg, rgba(20,22,45,.55) 0%, rgba(20,22,45,0) 60%),
      repeating-linear-gradient(90deg,
        var(--stripe-dark) 0 80px,
        var(--stripe-mid) 80px 100px,
        var(--stripe-light) 100px 150px,
        var(--stripe-mid) 150px 161px);
  }
  .silver-rule {
    position: absolute; left: 0; width: 861px; height: 14px;
    background: linear-gradient(90deg, var(--silver-dark), var(--silver-light) 50%, var(--silver-dark));
    border-top: 1px solid #2a2a2e; border-bottom: 1px solid #2a2a2e;
  }
  .silver-rule--1 { top: 118px; }
  .silver-rule--2 { top: 390px; }
  .silver-rule--3 { top: 980px; }
  .title-art { position: absolute; left: 0; top: 132px; }
  .volume-art { position: absolute; left: 0; top: 404px; }
  .features { position: absolute; left: 60px; top: 530px; list-style: none; }
  .feature {
    display: flex; align-items: center; height: 84px;
    font-family: "Merriweather", Georgia, serif; font-weight: 700;
    font-size: 31px; color: var(--white);
  }
  .feature svg { width: 72px; height: 60px; margin-right: 28px; flex: none; }
  .brand-plate {
    position: absolute; left: 260px; top: 1044px; width: 340px; height: 108px;
    background: var(--white); border: 3px solid var(--ink);
    display: flex; align-items: center; justify-content: center;
    font-family: "Merriweather", Georgia, serif; font-weight: 700;
    font-size: 32px; color: var(--ink);
  }
</style>
</head>
<body>
<main class="cover">
  <div class="stripe-band stripe-band--top"></div>
  <div class="silver-rule silver-rule--1"></div>

  <svg class="title-art" width="861" height="260" viewBox="0 0 861 260">
    <defs>
      <linearGradient id="chrome" x1="0" y1="0" x2="0" y2="1">
        <stop offset="0" stop-color="#ffffff"/>
        <stop offset=".45" stop-color="#f0f0f0"/>
        <stop offset=".8" stop-color="#8d8d92"/>
        <stop offset="1" stop-color="#55565c"/>
      </linearGradient>
    </defs>
    <text x="36" y="224" textLength="788" lengthAdjust="spacingAndGlyphs"
          font-family="Anton, Impact, sans-serif" font-size="262"
          fill="url(#chrome)" stroke="#1d1f3a" stroke-width="2">PHYSICS</text>
  </svg>

  <div class="silver-rule silver-rule--2"></div>

  <svg class="volume-art" width="861" height="130" viewBox="0 0 861 130">
    <defs>
      <linearGradient id="metal" x1="0" y1="0" x2="0" y2="1">
        <stop offset="0" stop-color="#ffffff"/>
        <stop offset=".5" stop-color="#d6d6d8"/>
        <stop offset="1" stop-color="#9a9aa0"/>
      </linearGradient>
    </defs>
    <text x="460" y="112" textLength="276" lengthAdjust="spacingAndGlyphs"
          font-family="Cinzel, Georgia, serif" font-weight="600" font-size="66"
          fill="url(#metal)" stroke="#4a4a52" stroke-width="1.2">VOLUME</text>
    <text x="770" y="112" font-family="Cinzel, Georgia, serif" font-weight="600" font-size="120"
          fill="url(#metal)" stroke="#4a4a52" stroke-width="1.5">1</text>
  </svg>

  <ul class="features">
    <li class="feature">
      <svg viewBox="0 0 72 60" fill="none" stroke="#fff" stroke-width="3" stroke-linejoin="round">
        <path d="M30 18a24 18 0 1 1 -14 32l-10 4 4-9a24 18 0 0 1 20-27z" transform="translate(2 -12)"/>
        <path d="M48 24a20 15 0 0 1 10 27l4 8-10-4a20 15 0 0 1 -14-3"/>
        <text x="14" y="30" font-family="Arial, sans-serif" font-size="15" font-weight="700" fill="#fff" stroke="none">Q&amp;A</text>
      </svg>
      Questions &amp; Answers
    </li>
    <li class="feature">
      <svg viewBox="0 0 72 60" fill="none" stroke="#fff" stroke-width="3.5" stroke-linejoin="round" stroke-linecap="round">
        <path d="M40 8H10v48h48V28"/>
        <path d="M58 4l8 8-28 28-11 3 3-11z"/>
      </svg>
      Theory Notes
    </li>
    <li class="feature">
      <svg viewBox="0 0 72 60" fill="none" stroke="#fff" stroke-width="3" stroke-linecap="round">
        <path d="M30 44c0-8-8-10-8-20a12 12 0 0 1 24 0c0 10-8 12-8 20z"/>
        <path d="M29 49h10M30 54h8"/>
        <path d="M34 2v5M14 10l4 4M54 10l-4 4M8 26h5M60 26h-5M14 42l4-3M54 42l-4-3"/>
      </svg>
      Tips &amp; Tricks
    </li>
    <li class="feature">
      <svg viewBox="0 0 72 60" fill="none" stroke="#fff" stroke-width="3.5" stroke-linecap="round" stroke-linejoin="round">
        <path d="M14 38a22 22 0 1 0 2-22"/>
        <path d="M10 10l6 7 8-4"/>
        <path d="M36 16v16l-8 6"/>
      </svg>
      Previous Year’s Reference Questions
    </li>
    <li class="feature">
      <svg viewBox="0 0 72 60" fill="none" stroke="#fff" stroke-width="2.5" stroke-linecap="round" stroke-linejoin="round">
        <rect x="14" y="8" width="30" height="44" rx="2"/>
        <path d="M24 5h10v6H24z"/>
        <path d="M19 20l3 3 4-5M29 21h10M19 31l3 3 4-5M29 32h10M19 42l3 3 4-5M29 43h6"/>
        <circle cx="46" cy="46" r="7" fill="#fff"/>
        <path d="M43 46l2 2 4-4" stroke="#2c3166"/>
      </svg>
      Cover Complete Syllabus
    </li>
  </ul>

  <div class="silver-rule silver-rule--3"></div>
  <div class="stripe-band stripe-band--bottom"></div>

  <div class="brand-plate">VORLIN Education</div>
</main>
</body>
</html>
```